Harborline Washtek Laundry Service Company

I own a Coin Operated laundry business and need to include a picture of Coin operated machines.
Include:
Company Name: Harborline Washtek
For all your Coin Operated Laundry needs.Include: sales, service, and new installations with commissions as high as 50%
include 1187 N. Larkview Rd, Arcadia, Ca 90417
626-518-2790
Include: Contact: Dwight Menser

Target Market(s)

coin Laundry

Industry/Entity Type

Business

Requirements
Must have
• picture of machines
• Sales, Service, Installations

```html
<!DOCTYPE html>
<html lang="en">
<head>
<meta charset="utf-8">
<title>Harborline Washtek – Coin Operated Laundry Flyer</title>
<link rel="stylesheet" href="https://fonts.googleapis.com/css2?family=Cabin:wght@400;500;600;700&family=Lobster&display=swap">
<style>
  :root {
    --page: #e9e7e3;
    --gold: #c4a85c;
    --gold-deep: #b8994c;
    --cream: #f1e6c4;
    --cream-soft: #e6d49f;
    --brown: #3f2f25;
    --ink: #3a2a1f;
    --white: #ffffff;
    --wall: #c89a6c;
    --wall-light: #e0bd93;
    --steel-dark: #4a4a4a;
    --steel-light: #e8e8e8;
  }
  * { margin: 0; padding: 0; box-sizing: border-box; }
  html, body { width: 1200px; height: 900px; overflow: hidden; }
  body {
    background: var(--page);
    font-family: "Cabin", sans-serif;
    position: relative;
  }
  .flyer {
    position: absolute;
    left: 75px; top: 100px;
    width: 1050px; height: 700px;
    overflow: hidden;
    box-shadow: 0 10px 30px rgba(0,0,0,.18);
    background: var(--gold);
  }
  .flyer-shapes { position: absolute; inset: 0; }
  .headline {
    position: absolute;
    left: 48px; top: 44px;
    color: var(--white);
    line-height: .95;
  }
  .headline .script {
    font-family: "Lobster", cursive;
    font-size: 64px;
    font-weight: 400;
    display: block;
    margin-left: 10px;
  }
  .headline .line {
    font-size: 52px;
    font-weight: 500;
    display: block;
  }
  .intro {
    position: absolute;
    left: 140px; top: 232px;
    width: 420px;
    font-size: 25px;
    line-height: 1.18;
    color: var(--ink);
    font-weight: 500;
  }
  .offer {
    position: absolute;
    left: 160px; top: 350px;
    color: var(--ink);
    line-height: .95;
  }
  .offer span { display: block; font-size: 50px; font-weight: 500; }
  .offer .rate { margin-left: 90px; font-size: 54px; }
  .contact {
    position: absolute;
    left: 60px; top: 566px;
    color: var(--white);
    font-size: 25px;
    font-weight: 700;
    font-style: normal;
    line-height: 1.3;
  }
  .phone {
    position: absolute;
    left: 680px; top: 548px;
    width: 370px;
    text-align: center;
    white-space: nowrap;
    color: var(--white);
    font-size: 50px;
    font-weight: 700;
    letter-spacing: 1px;
  }
</style>
</head>
<body>
  <main class="flyer">
    <svg class="flyer-shapes" width="1050" height="700" viewBox="0 0 1050 700">
      <defs>
        <linearGradient id="machineGrad" x1="0" y1="0" x2="1" y2="1">
          <stop offset="0" stop-color="var(--wall-light)"/>
          <stop offset=".45" stop-color="var(--wall)"/>
          <stop offset=".6" stop-color="#f2f2f0"/>
          <stop offset="1" stop-color="#dcdcda"/>
        </linearGradient>
        <linearGradient id="panelGrad" x1="0" y1="0" x2="1" y2=".6">
          <stop offset="0" stop-color="var(--gold-deep)"/>
          <stop offset=".45" stop-color="var(--cream-soft)"/>
          <stop offset="1" stop-color="var(--cream)"/>
        </linearGradient>
        <linearGradient id="steelGrad" x1="0" y1="0" x2="1" y2="1">
          <stop offset="0" stop-color="var(--steel-dark)"/>
          <stop offset=".5" stop-color="var(--steel-light)"/>
          <stop offset="1" stop-color="var(--steel-dark)"/>
        </linearGradient>
      </defs>
      <rect class="machine-photo" x="300" y="0" width="750" height="470" fill="url(#machineGrad)" role="img" aria-label="Photo of stacked coin operated washer and dryer machines in a laundromat"/>
      <rect class="phone-band" x="680" y="460" width="370" height="240" fill="var(--gold)"/>
      <polygon class="steel-stripe" points="262,0 300,0 700,460 680,480" fill="url(#steelGrad)"/>
      <polygon class="info-panel" points="0,0 262,0 680,480 680,700 0,700" fill="url(#panelGrad)"/>
      <polygon class="address-band" points="0,545 600,545 680,470 680,700 0,700" fill="var(--brown)"/>
      <polyline class="address-edge" points="0,545 600,545 680,470" fill="none" stroke="url(#steelGrad)" stroke-width="5"/>
    </svg>

    <h1 class="headline">
      <span class="script">Coin</span>
      <span class="line">Operated</span>
      <span class="line">laundry business</span>
    </h1>

    <p class="intro">For all your Coin Operated Laundry needs sales, service, and new installations with</p>

    <p class="offer">
      <span>commissions</span>
      <span class="rate">as high as 50%</span>
    </p>

    <address class="contact">
      Harborline Washtek<br>
      1187 N. Larkview Rd, Arcadia, Ca 90417<br>
      Contact: Dwight Menser
    </address>

    <p class="phone">626-518-2790</p>
  </main>
</body>
</html>
```